Business Card/Design Project for Personal Injury Lawyer

Personal Injury Attorney. I represent people who have been injured in accidents and are making money damage claims against the negligent party. As a personal injury attorney, I am a counselor, advisor, and legal representative to my clients. Clients want someone who is aggresssive yet professional.

More information about what I do an be found at www.dravolinlaw.com

Target Market(s)

General public.

Industry/Entity Type

Legal

Contact Information for Business Card

Need a new logo/brand image for b-cards, website, and letterhead/envelops. Looking for something original (no scales of justice or courthouse columns), yet classy and professional.

Here's what I'm thinking (but I'm always open to other ideas):

On the front, I would like my name (Corwin T. Dravolin), and underneath the words "Personal Injury Attorney." The background could be black, for example, and the lettering could be white or foil. I'm open to differnt colors, or even two colors. My name on the front side should pop.

And then on the back would be all my contact info, and maybe a logo or a slogan.

Here are two slogans I've come up with so far: 1. Settle for More. 2. Strong Counsel for Every Injured Client.

Requirements
Must have
• Something that identifys me as a personal injury attorney, such as the words Personal Injury Attorney (or Lawyer, or Law Firm, etc.).
Nice to have
• A style/image that can be used nicely on my website and on letterhead.
Should not have
• Tired, commonly used logos or symbols, such a scales of justice or courthouse columns.

```html
<!DOCTYPE html>
<html lang="en">
<head>
<meta charset="utf-8">
<title>Dravolin Law – Business Card Back</title>
<link href="https://fonts.googleapis.com/css2?family=Open+Sans:wght@400;600&family=Tinos:wght@700&display=swap" rel="stylesheet">
<style>
  :root {
    --page-bg: #f2f2f2;
    --card-black: #0b0b0b;
    --ink-white: #ffffff;
    --icon-frame: #7a5a32;
    --social-blue: #3b5a96;
    --social-cyan: #27a7dc;
  }
  * { margin: 0; padding: 0; box-sizing: border-box; }
  html, body {
    width: 1200px; height: 1000px; overflow: hidden;
    background: var(--page-bg);
  }
  .card-back {
    position: absolute; left: 150px; top: 243px;
    width: 900px; height: 514px;
    background: var(--card-black);
    color: var(--ink-white);
    font-family: "Open Sans", Arial, sans-serif;
  }
  .contact-list { position: absolute; left: 132px; top: 144px; list-style: none; }
  .contact-item {
    display: flex; align-items: flex-start; gap: 9px;
    margin-bottom: 14px; font-size: 23px; line-height: 26px;
  }
  .contact-icon {
    flex: none; width: 28px; height: 28px;
    border: 1.5px solid var(--icon-frame);
    display: flex; align-items: center; justify-content: center;
  }
  .contact-icon svg { width: 18px; height: 18px; }
  .social-list { position: absolute; left: 125px; top: 354px; list-style: none; }
  .social-item {
    display: flex; align-items: center; gap: 10px;
    margin-bottom: 9px; font-size: 17px; line-height: 28px;
  }
  .social-square { width: 28px; height: 28px; }
  .social-square.page { background: var(--social-blue); }
  .social-square.feed { background: var(--social-cyan); }
  .firm-mark {
    position: absolute; left: 540px; top: 125px; width: 190px;
    display: flex; flex-direction: column; align-items: center; gap: 14px;
  }
  .firm-mark-circle {
    width: 130px; height: 130px; border-radius: 50%;
    border: 6px solid var(--ink-white);
  }
  .firm-mark-name { font-size: 24px; font-weight: 600; color: var(--ink-white); }
  .slogan {
    position: absolute; right: 206px; top: 440px;
    font-family: "Tinos", "Times New Roman", serif;
    font-weight: 700; font-size: 20px; line-height: 24px;
    white-space: nowrap;
  }
</style>
</head>
<body>
  <section class="card-back">
    <ul class="contact-list">
      <li class="contact-item">
        <span class="contact-icon"><svg viewBox="0 0 18 18"><path d="M2 7c0-3 14-3 14 0v2h-4V7.5H6V9H2z M4 10h10l1 5H3z" fill="#fff"/></svg></span>
        <span>305.555.0190</span>
      </li>
      <li class="contact-item">
        <span class="contact-icon"><svg viewBox="0 0 18 18"><rect x="2" y="4" width="14" height="10" fill="none" stroke="#fff" stroke-width="1.4"/><path d="M2 4l7 6 7-6" fill="none" stroke="#fff" stroke-width="1.4"/></svg></span>
        <span>305.555.0147</span>
      </li>
      <li class="contact-item">
        <span class="contact-icon"><svg viewBox="0 0 18 18"><circle cx="9" cy="9" r="7" fill="none" stroke="#fff" stroke-width="1.3"/><ellipse cx="9" cy="9" rx="3" ry="7" fill="none" stroke="#fff" stroke-width="1.1"/><path d="M2 9h14M3.5 5h11M3.5 13h11" stroke="#fff" stroke-width="1.1"/></svg></span>
        <span>www.dravolinlaw.com</span>
      </li>
      <li class="contact-item">
        <span class="contact-icon"><svg viewBox="0 0 18 18"><path d="M9 17C5 11 4 9 4 7a5 5 0 0 1 10 0c0 2-1 4-5 10z" fill="#fff"/><circle cx="9" cy="7" r="2" fill="#0b0b0b"/></svg></span>
        <span>2140 Larkspur Avenue<br>Suite 410<br>Harbor Beach, Florida 33100</span>
      </li>
    </ul>

    <ul class="social-list">
      <li class="social-item"><span class="social-square page"></span><span>www.friendpage.net/dravolin-law</span></li>
      <li class="social-item"><span class="social-square feed"></span><span>harborbeachlaw</span></li>
    </ul>

    <div class="firm-mark">
      <span class="firm-mark-circle"></span>
      <span class="firm-mark-name">Dravolin Law</span>
    </div>

    <p class="slogan">Strong Counsel for Every Injured Client.</p>
  </section>
</body>
</html>
```